Fitness Body Weight Exercises Book Cover

Need a book cover design for a new book

This book is going to market to people to get in shape by playing a fitness dice game call FlexRUMBA The dice game

When people see the cover they should see that this is a book that can help them get in shape. We are positioning the guru as an expert inside of the fitness niche

Target Market(s)

fitness

Requirements
Must have
• The name of the book which is

"The Grand Victor Floorwork Regimen"

Tagline -

The Worlds #1 Resource For Combat Strength Training Using Body Weight Exercises For Men, Women and Children

__________

Featuring FlexRUMBA The Dice Game (TM)

___________________________
ON THE BACK COVER

Image with Bren with his gold medal
with these words
No Weights, No Problem

_____-

front cover
the image with him doing a push up should be on the front of the cover with these words

_________
Nice to have
• Maybe

"Bren Presents ...."

The Grand Victor Floorwork Regimen

```html
<!DOCTYPE html>
<html lang="en">
<head>
<meta charset="utf-8">
<title>The Grand Victor Floorwork Regimen – Book Cover</title>
<link rel="stylesheet" href="https://fonts.googleapis.com/css2?family=Bebas+Neue&family=Oswald:wght@500;600;700&family=Open+Sans:wght@700&display=swap">
<style>
  :root {
    --stage: #252525;
    --cover-dark: #0b0d12;
    --cover-mid: #1a1f2a;
    --gold-light: #f6dc9a;
    --gold: #c99a4a;
    --gold-deep: #a8732f;
    --white: #ffffff;
    --band-text: #1b1408;
    --photo-skin: #6b4a36;
  }
  * { box-sizing: border-box; margin: 0; padding: 0; }
  html, body {
    width: 1200px; height: 1200px; overflow: hidden;
    background: var(--stage);
  }
  .canvas { position: relative; width: 1200px; height: 1200px; }

  .cover-wrap {
    position: absolute; left: 14px; top: 178px; width: 1172px; height: 844px;
    background: radial-gradient(ellipse at 30% 35%, var(--cover-mid) 0%, var(--cover-dark) 70%);
    overflow: hidden;
  }

  .gold-text {
    background: linear-gradient(90deg, var(--gold-deep) 0%, var(--gold-light) 45%, var(--gold) 70%, var(--gold-deep) 100%);
    -webkit-background-clip: text; background-clip: text; color: transparent;
  }

  /* back cover */
  .back-headline {
    position: absolute; left: 68px; top: 60px;
    font-family: 'Bebas Neue', 'Oswald', sans-serif;
    font-size: 84px; line-height: 0.92; letter-spacing: 1px;
    transform: rotate(-4deg); transform-origin: left top;
    z-index: 2;
  }
  .back-photo {
    position: absolute; left: 70px; top: 206px; width: 444px; height: 572px;
    background: radial-gradient(ellipse at 50% 45%, #8a6048 0%, var(--photo-skin) 45%, rgba(30,24,22,0) 75%);
  }

  /* spine */
  .spine-title {
    position: absolute; left: 582px; top: 100px;
    writing-mode: vertical-rl;
    font-family: 'Oswald', sans-serif; font-weight: 500;
    font-size: 24px; letter-spacing: 6px; color: var(--gold);
  }

  /* front cover */
  .front {
    position: absolute; left: 646px; top: 0; width: 526px; height: 778px;
    text-align: center;
  }
  .presenter {
    margin-top: 22px;
    font-family: 'Oswald', sans-serif; font-weight: 600;
    font-size: 20px; letter-spacing: 9px; color: var(--gold);
  }
  .title { font-family: 'Oswald', sans-serif; font-weight: 700; line-height: 1; margin-top: 14px; }
  .title-the { display: block; font-size: 36px; color: var(--white); }
  .title-grand { display: block; font-size: 60px; margin-top: 4px; }
  .title-floor { display: block; font-size: 92px; color: var(--white); margin-top: 2px; letter-spacing: -1px; }
  .title-regimen { display: block; font-size: 122px; margin-top: -2px; letter-spacing: -1px; }
  .tagline {
    margin: 20px auto 0; width: 460px;
    font-family: 'Open Sans', sans-serif; font-weight: 700;
    font-size: 15px; line-height: 1.3; color: var(--white);
  }
  .tagline .accent { color: var(--gold); }
  .front-photo {
    position: absolute; left: 18px; top: 434px; width: 508px; height: 344px;
    background: linear-gradient(180deg, rgba(20,24,30,0) 0%, #3a3a3c 45%, #5e5a55 100%),
                radial-gradient(ellipse at 55% 55%, var(--photo-skin) 0%, rgba(0,0,0,0) 60%);
  }

  /* bottom band */
  .feature-band {
    position: absolute; left: 0; bottom: 0; width: 100%; height: 66px;
    background: linear-gradient(90deg, var(--gold-deep) 0%, var(--gold-light) 25%, var(--gold) 50%, var(--gold-light) 75%, var(--gold-deep) 100%);
  }
  .feature-text {
    position: absolute; right: 60px; top: 14px;
    font-family: 'Oswald', sans-serif; font-weight: 600;
    font-size: 28px; color: var(--band-text); letter-spacing: 0.5px;
  }
</style>
</head>
<body>
<div class="canvas">
  <div class="cover-wrap">
    <section class="back-cover">
      <div class="back-photo" role="img" aria-label="Photo of Bren, smiling and shirtless, wearing a backwards cap and a gold medal"></div>
      <h2 class="back-headline gold-text">No Weights,<br>No Problem</h2>
    </section>

    <div class="spine-title">THE GRAND VICTOR FLOORWORK REGIMEN</div>

    <section class="front">
      <p class="presenter">BREN PRESENTS</p>
      <h1 class="title">
        <span class="title-the">THE</span>
        <span class="title-grand gold-text">GRAND VICTOR</span>
        <span class="title-floor">FLOORWORK</span>
        <span class="title-regimen gold-text">REGIMEN</span>
      </h1>
      <p class="tagline">The <span class="accent">Worlds #1 Resource</span> For Combat Strength Training Using Body Weight Exercises For Men, Women and Children</p>
      <div class="front-photo" role="img" aria-label="Photo of Bren doing a push-up on a concrete floor"></div>
    </section>

    <div class="feature-band">
      <p class="feature-text">FEATURING FLEXRUMBA THE DICE GAME (TM)</p>
    </div>
  </div>
</div>
</body>
</html>
```